TBL Surveyors

I am a CPVA Chartered Building Surveyor and Registered Valuer carry out traditional Building Surveying work in Yorkshire UK and in Tarn, France. I do structural surveys, measured surveys and CAD drawing, Home Buyer surveys, Project Management, Building Refurbishment advice. My Speciality is historic and listed buildings. I specify traditional materials. I do not hide behind endless caveats or stock phrases in my reports.

I want a design which will work in Estate Agents offices aimed at the demograph likely to use my services, so 30 - 60. I don't want it to be too stuffy, or safe, but it needs to show professionalism.

Needs to include CPVA Logos and my Siret number for France which is 437 918 062

Web address www.tbl-surveyors.example (not yet live)
email ; gareth@tbl-surveyors.example

```html
<!DOCTYPE html>
<html lang="en">
<head>
<meta charset="utf-8">
<title>TBL Surveyors – Flyer</title>
<link rel="stylesheet" href="https://fonts.googleapis.com/css2?family=Lato:wght@400;700;900&family=Roboto+Condensed:wght@400;700&display=swap">
<style>
  :root {
    --ink: #111111;
    --ink-soft: #333333;
    --black: #050505;
    --white: #ffffff;
    --silver-light: #fbfbfb;
    --pill-grey: #c9c9c9;
    --brand-blue: #1e86c8;
    --number-blue: #1c6fa8;
    --icon-blue: #3ea3d9;
    --plan-grey: #ececec;
  }
  * { box-sizing: border-box; margin: 0; padding: 0; }
  html, body { width: 1200px; height: 900px; overflow: hidden; background: var(--white); }
  .flyer { position: relative; width: 1200px; height: 900px; overflow: hidden; font-family: "Lato", sans-serif; }
  .flyer__shapes { position: absolute; inset: 0; }

  .header {
    position: absolute; left: 0; top: 0; width: 1200px; height: 130px;
    display: flex; align-items: center; justify-content: space-between;
    padding: 0 62px 0 48px;
  }
  .brand { display: flex; align-items: center; gap: 22px; }
  .brand__mark { width: 78px; height: 78px; background: var(--brand-blue); }
  .brand__name { font-weight: 400; font-size: 34px; color: var(--ink-soft); }
  .header__title {
    font-family: "Roboto Condensed", sans-serif; font-size: 38px; color: var(--ink);
    font-weight: 400; letter-spacing: 0.3px;
  }
  .header__title strong { font-weight: 700; }

  .services__pill {
    position: absolute; left: 60px; top: 130px; width: 344px; height: 77px;
    border-radius: 0 0 26px 26px;
    background: linear-gradient(180deg, var(--silver-light), var(--pill-grey));
    box-shadow: 0 3px 6px rgba(0,0,0,0.35);
    display: flex; align-items: center; justify-content: center;
    font-weight: 700; font-size: 40px; color: var(--ink);
  }
  .services__list {
    position: absolute; left: 88px; top: 253px; width: 350px; list-style: none;
    color: var(--ink); font-size: 31px; line-height: 1.0;
  }
  .services__list li { margin-bottom: 21px; }

  .siret {
    position: absolute; left: 62px; top: 584px; width: 370px; height: 96px;
    border-radius: 22px;
    background: linear-gradient(180deg, var(--silver-light), var(--pill-grey));
    box-shadow: 0 3px 8px rgba(0,0,0,0.35);
    text-align: center; padding-top: 6px;
  }
  .siret__label { font-weight: 700; font-size: 25px; color: var(--ink-soft); }
  .siret__number { font-weight: 700; font-size: 50px; line-height: 1.05; color: var(--number-blue); letter-spacing: 1px; }

  .contact { position: absolute; left: 44px; top: 782px; color: var(--white); font-weight: 700; font-size: 25px; font-style: normal; }
  .contact__row { display: flex; align-items: center; gap: 16px; height: 40px; }
  .contact__row svg { width: 30px; height: 30px; flex: none; }
</style>
</head>
<body>
<div class="flyer">
  <svg class="flyer__shapes" width="1200" height="900" viewBox="0 0 1200 900" xmlns="http://www.w3.org/2000/svg">
    <defs>
      <linearGradient id="silverBar" x1="0" y1="0" x2="0" y2="1">
        <stop offset="0" stop-color="#6b6b6b"/>
        <stop offset="0.12" stop-color="#f2f2f2"/>
        <stop offset="0.55" stop-color="#ffffff"/>
        <stop offset="0.88" stop-color="#c4c4c4"/>
        <stop offset="1" stop-color="#8c8c8c"/>
      </linearGradient>
      <radialGradient id="bluePanel" cx="0.55" cy="0.7" r="0.8">
        <stop offset="0" stop-color="#8fd3f1"/>
        <stop offset="0.55" stop-color="#3ea3d9"/>
        <stop offset="1" stop-color="#1677b8"/>
      </radialGradient>
      <linearGradient id="photoTone" x1="0" y1="0" x2="1" y2="1">
        <stop offset="0" stop-color="#b58a5f"/>
        <stop offset="0.5" stop-color="#e2d8cb"/>
        <stop offset="1" stop-color="#a9774b"/>
      </linearGradient>
    </defs>

    <rect x="0" y="0" width="1200" height="900" fill="var(--black)"/>
    <polygon points="0,130 512,130 512,645 470,740 0,740" fill="url(#bluePanel)"/>
    <rect x="0" y="740" width="470" height="12" fill="var(--white)"/>

    <rect x="512" y="130" width="688" height="515" fill="url(#photoTone)" role="img" aria-label="Photo: two people at a desk with plans, clipboard, phone, calculator, spirit level and wood samples"/>

    <polygon points="543,645 782,645 721,900 476,900" fill="var(--white)"/>
    <polygon points="556,668 770,668 718,880 505,880" fill="var(--plan-grey)" role="img" aria-label="Technical drawing: annotated building section"/>
    <polygon points="795,645 1200,645 1200,900 734,900" fill="var(--white)"/>
    <polygon points="810,672 1185,672 1185,880 762,880" fill="var(--plan-grey)" role="img" aria-label="Technical drawing: floor plan of a dwelling"/>

    <rect x="0" y="0" width="1200" height="130" fill="url(#silverBar)"/>
  </svg>

  <header class="header">
    <div class="brand">
      <span class="brand__mark"></span>
      <span class="brand__name">TBL Surveyors</span>
    </div>
    <h1 class="header__title"><strong>CPVA CHARTERED</strong> BUILDING SURVEYOR</h1>
  </header>

  <h2 class="services__pill">Services</h2>
  <ul class="services__list">
    <li>structural surveys</li>
    <li>measured surveys and CAD drawing</li>
    <li>Home Buyer surveys</li>
    <li>Project Management</li>
    <li>Building Refurbishment advice</li>
  </ul>

  <div class="siret">
    <div class="siret__label">Siret number for France</div>
    <div class="siret__number">437 918 062</div>
  </div>

  <address class="contact">
    <div class="contact__row">
      <svg viewBox="0 0 28 28"><rect x="3" y="7" width="22" height="15" rx="1" fill="var(--icon-blue)"/><polyline points="3,7 14,16 25,7" fill="none" stroke="#ffffff" stroke-width="1.6"/></svg>
      <span>gareth@tbl-surveyors.example</span>
    </div>
    <div class="contact__row">
      <svg viewBox="0 0 28 28"><circle cx="14" cy="14" r="11" fill="none" stroke="var(--icon-blue)" stroke-width="2.4"/><ellipse cx="14" cy="14" rx="5" ry="11" fill="none" stroke="var(--icon-blue)" stroke-width="1.8"/><line x1="3" y1="14" x2="25" y2="14" stroke="var(--icon-blue)" stroke-width="1.8"/></svg>
      <span>www.tbl-surveyors.example</span>
    </div>
  </address>
</div>
</body>
</html>
```